Brochure Design Project

Need to create a brochure/product information material for a Therapy Product.

Please find attached the file:
- this has all the information for the product, if you for visual affect need to remove some of the content please ensure you don't remove key information.

please use these items or create your own level bar if you feel it needs to look different to match better.

Please ensure you use Coral Framing Logo and RVK Logo.

will need to fit on a A4 folded double sided brochure
Updates

Hi All,

please be aware that i have updated some text. i have attached a new updated version of the brief with the changed text in bold and underlined. there are three sections where i have added and made changes. please ensure you make these changes to your designs also. Thank you for your submissions they all look great so far. 

Target Market(s)

Community Services, Child Protection, Youth Work, Schools, At-Risk Youth Orangisations

Industry/Entity Type

Product

Requirements
Must have
• Must have core information provided, be visually appealing.

```html
<!DOCTYPE html>
<html lang="en">
<head>
<meta charset="utf-8">
<title>RVK Brochure – How it Works</title>
<link href="https://fonts.googleapis.com/css2?family=Source+Sans+3:wght@300;400;600&display=swap" rel="stylesheet">
<style>
  :root{
    --backdrop:#2b2b2b;
    --paper:#ffffff;
    --fold:#d9d9d9;
    --ink:#2a2a2a;
    --ink-soft:#4a4a4a;
    --respect:#e6a912;
    --safe:#a8c41c;
    --achieve:#78bf6c;
    --learn:#6ec6d9;
    --dash-warm:#e6a912;
    --dash-cool:#6ec6d9;
    --note-bg:#f5e6c8;
    --note-line:#d8a84a;
    --process-red:#c8302c;
    --step-1:#cfcfcf;
    --step-2:#a9a9a9;
    --step-3:#7f7f7f;
    --footer:#0d0d0d;
    --footer-mail:#e6a912;
    --footer-social:#6ec6d9;
    --bar-green:#8fd12a;
  }
  *{box-sizing:border-box;margin:0;padding:0}
  html,body{width:1200px;height:793px;overflow:hidden}
  body{background:var(--backdrop);font-family:"Source Sans 3",Arial,sans-serif;color:var(--ink);position:relative}
  .spread{position:absolute;left:108px;top:48px;width:977px;height:692px;background:var(--paper)}
  .page{position:absolute;top:0;height:657px}
  .page--left{left:0;width:490px;background:linear-gradient(90deg,var(--paper) 65%,var(--fold) 100%)}
  .page--right{left:490px;width:487px;background:linear-gradient(90deg,#e6e6e6 0%,var(--paper) 12%)}
  .abs{position:absolute}
  .title{left:34px;top:24px;font-size:46px;font-weight:300;letter-spacing:-.5px;line-height:1.2;color:var(--ink)}
  .frame{left:18px;top:68px}
  .intro{left:35px;top:82px;width:255px;font-size:12.6px;line-height:1.38;color:var(--ink-soft)}
  .guideline{width:86px;height:86px;border-radius:50%;top:193px;display:flex;align-items:center;justify-content:center;text-align:center;color:#fff;font-size:16.5px;font-weight:300;line-height:1.25;text-transform:uppercase}
  .guideline--respect{left:55px;background:var(--respect)}
  .guideline--safe{left:151px;background:var(--safe)}
  .guideline--achieve{left:250px;background:var(--achieve)}
  .guideline--learn{left:353px;background:var(--learn)}
  .lead{font-size:13.5px;font-weight:400;text-transform:uppercase;line-height:1.1;color:var(--ink)}
  .body{font-size:10.6px;line-height:1.38;color:var(--ink)}
  .reflect{left:39px;top:319px;width:408px}
  .rewards{left:39px;top:464px;width:415px}
  .level-bar{left:67px;top:574px}
  .weekly{left:39px;top:37px;width:430px}
  .weekly .body{font-size:9.6px}
  .note{left:29px;top:115px;width:438px;height:114px;background:var(--note-bg);border:1px dashed var(--note-line)}
  .note-art{left:6px;top:5px;width:52px;height:100px;border-radius:6px;background:linear-gradient(180deg,#e47a2a,#7a7a7a)}
  .note-text{left:47px;top:10px;width:358px;font-size:9.6px;line-height:1.36}
  .note-text .lead{font-size:11.5px}
  .change{left:39px;top:238px;width:430px;font-size:7.6px;line-height:1.5}
  .group-photo{left:10px;top:290px;width:477px;height:125px;background:linear-gradient(180deg,#efe6dc,#e9ddd2 55%,#f4f1ee);border-radius:2px}
  .process-title{left:15px;top:420px;font-size:25px;font-weight:300;line-height:1.2;color:var(--process-red)}
  .process-text{left:19px;top:454px;width:452px;font-size:9.4px;line-height:1.38;color:var(--ink-soft)}
  .steps{left:29px;top:530px}
  .footer{position:absolute;left:0;top:657px;width:977px;height:35px;background:var(--footer);color:#fff;font-size:10px;display:flex;align-items:center}
  .footer-item{position:absolute}
  .footer-mail{left:35px;color:var(--footer-mail)}
  .footer-sep{color:#ddd}
  .footer-sep--one{left:183px}
  .footer-social{left:213px;color:var(--footer-social)}
  .footer-sep--two{left:303px}
  .footer-web{left:330px}
  .footer .brand{left:652px;display:flex;align-items:center;gap:9px;font-size:16px;letter-spacing:1.4px;font-weight:400;color:#fff}
  .brand-mark{width:13px;height:13px;border:1.5px solid #fff}
</style>
</head>
<body>
<div class="spread">
  <section class="page page--left">
    <h1 class="abs title">How it Works?</h1>
    <svg class="abs frame" width="452" height="226" viewBox="0 0 452 226">
      <path d="M18 1 H1 V223 H40" fill="none" stroke="var(--dash-warm)" stroke-dasharray="4 3"/>
      <path d="M150 1 H449 V223 H436" fill="none" stroke="var(--dash-cool)" stroke-dasharray="4 3"/>
    </svg>
    <p class="abs intro">The core engine of RVK is when the Player and the GameMaster (GM) run through an intentional daily reflection conversation reviewing the highlights and challenging moments throughout the day across the four guidelines:</p>
    <div class="abs guideline guideline--respect">Respect</div>
    <div class="abs guideline guideline--safe">Staying<br>Safe</div>
    <div class="abs guideline guideline--achieve">Achieving</div>
    <div class="abs guideline guideline--learn">Learning</div>
    <div class="abs reflect">
      <p class="lead">These are based on the working agreement and are the daily reflections that use the experiential learning cycle.</p>
      <p class="body">The GM inputs the reflected experience point score out of 5 per criteria. Honesty is encourages along with genuine reflection on the events of the day. The goal is to simply reflect on the day. This Reflection works of the premise of empowerment of the child/young person evaluation of self and then the earning of rewards is positive reinforcement for the right behaviours. This reflective conversation between the Player and the GM need to be strength based.</p>
    </div>
    <p class="abs body rewards">The points go towards rewards that can be redeemed at the end of each cycle (usually weekly). The player also gains Experience Points towards their Level Bar.<br>Throughout the play period every 3-6 months a significant Real World Reward can be obtain if a certain Level cap is achieved.</p>
    <svg class="abs level-bar" width="343" height="30" viewBox="0 0 343 30" role="img" aria-label="Level bar">
      <rect x="0.5" y="0.5" width="342" height="29" rx="2" fill="#1c1c1c" stroke="#555"/>
      <rect x="8" y="8" width="265" height="14" rx="3" fill="#2e2e2e"/>
      <rect x="9" y="9" width="187" height="12" rx="3" fill="var(--bar-green)"/>
      <circle cx="70" cy="12" r="2" fill="#e8ff9a"/>
      <rect x="278" y="7" width="56" height="16" rx="2" fill="#2a2a2a"/>
      <text x="283" y="19" font-family="Source Sans 3, Arial, sans-serif" font-size="9.5" font-weight="600" fill="#fff">LEVEL BAR</text>
    </svg>
  </section>

  <section class="page page--right">
    <div class="abs weekly">
      <p class="lead">Each week depending on how many points the player has earned they win the associated rewards with the points gained for the week.</p>
      <p class="body">The player can change their reward when a new cycle starts. Rewards are budgeted against the points gained. If a player averages 35 they will get a much better reward than averaging 5.</p>
    </div>
    <div class="abs note">
      <div class="abs note-art" role="img" aria-label="Illustration of a toy car and a hammer badge"></div>
      <p class="abs note-text"><span class="lead">RVK also provides a badges system and title system.</span> The badge system allows for the players motivation around collection, achievement and social play. Some Badges also reward in Game items. The Challenges associated with earning Badges are for completing significant development achievement, educational/employment success and independent living skills being displayed. The Title System again allows of a level of peer appreciation for fellow players progress and builds a great reputational drive for the player sense of self and status amongst peers.</p>
    </div>
    <p class="abs change">This intervention is about creating long-term change in behaviour and attitude. It is designed to be highly engaging to the young person and focuses on real growth and change in the individual.</p>
    <div class="abs group-photo" role="img" aria-label="Photo of five smiling young people leaning over a white banner"></div>
    <h2 class="abs process-title">The Process:</h2>
    <p class="abs process-text">To get the best out of RVK, Coral Framing want to know what you are already doing this involves an initial consultation to review current Practice Frameworks and Models for service delivery you use to allow for greater integration with RVK, and to provide you with further information on RVK look at examples and assess whether this Therapeutic Intervention is for your service. The process then involves making changes to fit with your frameworks and then training and implementation into your service delivery.</p>
    <svg class="abs steps" width="436" height="110" viewBox="0 0 436 110" font-family="Source Sans 3, Arial, sans-serif" font-weight="300">
      <path d="M285 2 H427 Q434 2 434 9 V100 Q434 107 427 107 H285 L310 55 Z" fill="var(--step-3)"/>
      <path d="M120 2 H285 L310 55 L285 107 H120 L145 55 Z" fill="var(--step-2)"/>
      <path d="M7 14 H120 L145 55 L120 96 H7 Q0 96 0 89 V21 Q0 14 7 14 Z" fill="var(--step-1)"/>
      <text x="76" y="60" text-anchor="middle" font-size="16.5" fill="#555">Inital Consultation</text>
      <text x="219" y="42" text-anchor="middle" font-size="16.5" fill="#eee">Setup Design</text>
      <text x="219" y="60" text-anchor="middle" font-size="16.5" fill="#eee">and</text>
      <text x="219" y="78" text-anchor="middle" font-size="16.5" fill="#eee">Development</text>
      <text x="364" y="44" text-anchor="middle" font-size="16.5" fill="#fff">Training</text>
      <text x="364" y="62" text-anchor="middle" font-size="16.5" fill="#fff">and</text>
      <text x="364" y="80" text-anchor="middle" font-size="16.5" fill="#fff">implementation</text>
    </svg>
  </section>

  <footer class="footer">
    <span class="footer-item footer-mail">e: enquires@coralframing.com</span>
    <span class="footer-item footer-sep footer-sep--one">|</span>
    <span class="footer-item footer-social">t: @coralframing</span>
    <span class="footer-item footer-sep footer-sep--two">|</span>
    <span class="footer-item footer-web">w: www.coralframing.com</span>
    <span class="footer-item brand"><span class="brand-mark"></span>CoralFraming</span>
  </footer>
</div>
</body>
</html>
```